Vesit cards for web development company

We need a business card design for our company. The company develops online platforms and conducts marketing consulting. Company logo. The cards must fit in with us (a junior start UP), but they must also be professional enough to impress with investors like banks. We wish you a combination of classic and modern design

Target Market(s)

Business partners and IT and marketing customers

Industry/Entity Type

It Company

Contact Information for Business Card

Folgende Information müssen Drauf.
Name, Position, Telefon Nr., Mobile Nr., E-Mail adresse, Optional sind noch Webadresse und HRB Nummer

Colors

Designer to choose colors to be used in the design.

Requirements
Must have
• The cards have to fit into the logo later and have to be dynamic and serious at the same time

```html
<!DOCTYPE html>
<html lang="en">
<head>
<meta charset="utf-8">
<title>Novara Development – Business Card</title>
<link rel="stylesheet" href="https://fonts.googleapis.com/css2?family=Roboto+Condensed:wght@400;700&family=Roboto:wght@400;500&display=swap">
<style>
  :root {
    --backdrop: #2b2b2d;
    --card: #f3f3f3;
    --brand-blue: #1272b8;
    --brand-grey: #8e8f93;
    --text-light: #ffffff;
    --text-muted: #555558;
  }
  * { margin: 0; padding: 0; box-sizing: border-box; }
  html, body {
    width: 1200px; height: 960px; overflow: hidden;
    background: var(--backdrop);
  }
  .canvas { position: relative; width: 1200px; height: 960px; }

  .card {
    position: absolute;
    width: 600px; height: 343px;
    background: var(--card);
    border-radius: 18px;
    overflow: hidden;
  }
  .card--front { left: 314px; top: 113px; }
  .card--back { left: 311px; top: 472px; }

  .card__top-strip {
    position: absolute; left: 0; top: 0; width: 100%; height: 12px;
    background: var(--brand-grey);
  }

  .wordmark {
    position: absolute; left: 0; width: 100%;
    display: flex; align-items: center; justify-content: center; gap: 12px;
    font-family: "Roboto Condensed", Arial, sans-serif;
    font-weight: 700; color: var(--brand-blue);
    text-transform: uppercase; letter-spacing: 1px;
  }
  .wordmark__dot {
    background: var(--brand-blue); border-radius: 50%;
  }
  .card--front .wordmark { top: 112px; font-size: 34px; }
  .card--front .wordmark__dot { width: 18px; height: 18px; }
  .card--back .wordmark { top: 130px; font-size: 48px; }
  .card--back .wordmark__dot { width: 26px; height: 26px; }

  .contact-band {
    position: absolute; left: 0; bottom: 0; width: 100%; height: 108px;
    background: var(--brand-blue);
    color: var(--text-light);
  }
  .person {
    position: absolute; left: 46px; top: 28px;
    font-family: "Roboto Condensed", Arial, sans-serif;
    text-transform: uppercase;
  }
  .person__name { font-size: 21px; font-weight: 700; line-height: 24px; }
  .person__role { font-size: 15px; font-weight: 400; line-height: 20px; }

  .divider {
    position: absolute; top: 30px; width: 1.5px; height: 38px;
    background: rgba(255,255,255,0.85);
  }
  .divider--first { left: 192px; }
  .divider--second { left: 360px; }

  .contact-list {
    position: absolute; top: 31px; list-style: none;
    font-family: Roboto, Arial, sans-serif; font-size: 14.5px;
  }
  .contact-list--phones { left: 220px; }
  .contact-list--online { left: 387px; }
  .contact-list li {
    display: flex; align-items: center; gap: 7px; height: 20px;
  }
  .contact-list svg { width: 13px; height: 13px; fill: var(--text-light); flex: none; }

  .site-address {
    position: absolute; left: 0; top: 289px; width: 100%;
    text-align: center;
    font-family: Roboto, Arial, sans-serif; font-size: 15px;
    letter-spacing: 5px; color: var(--text-muted);
  }
</style>
</head>
<body>
<main class="canvas">

  <section class="card card--front" aria-label="Business card front">
    <div class="card__top-strip"></div>
    <div class="wordmark"><span class="wordmark__dot"></span>Novara Development</div>

    <div class="contact-band">
      <div class="person">
        <p class="person__name">Lukas Brenner</p>
        <p class="person__role">CEO/Founder</p>
      </div>

      <span class="divider divider--first"></span>

      <ul class="contact-list contact-list--phones">
        <li>
          <svg viewBox="0 0 24 24" aria-hidden="true"><path d="M6.6 10.8a15.1 15.1 0 0 0 6.6 6.6l2.2-2.2c.3-.3.7-.4 1-.2 1.1.4 2.3.6 3.6.6.6 0 1 .4 1 1V20c0 .6-.4 1-1 1A17 17 0 0 1 3 4c0-.6.4-1 1-1h3.5c.6 0 1 .4 1 1 0 1.3.2 2.5.6 3.6.1.3 0 .7-.2 1z"/></svg>
          614 205 7391
        </li>
        <li>
          <svg viewBox="0 0 24 24" aria-hidden="true"><path d="M7 1h10a2 2 0 0 1 2 2v18a2 2 0 0 1-2 2H7a2 2 0 0 1-2-2V3a2 2 0 0 1 2-2zm0 3v14h10V4zm5 15.5a1 1 0 1 0 0 2 1 1 0 0 0 0-2z"/></svg>
          742 918 3056
        </li>
      </ul>

      <span class="divider divider--second"></span>

      <ul class="contact-list contact-list--online">
        <li>
          <svg viewBox="0 0 24 24" aria-hidden="true"><path d="M2 5h20v14H2zm2 2v.4l8 5.2 8-5.2V7zm0 2.8V17h16V9.8l-8 5.2z"/></svg>
          hello@novaradev.com
        </li>
        <li>
          <svg viewBox="0 0 24 24" aria-hidden="true"><path d="M12 2a10 10 0 1 0 0 20 10 10 0 0 0 0-20zm6.9 6h-3a15 15 0 0 0-1.3-3.9A8 8 0 0 1 18.9 8zM12 4c.8 1.2 1.5 2.5 1.9 4h-3.8c.4-1.5 1.1-2.8 1.9-4zM4.3 14a8 8 0 0 1 0-4h3.4a16 16 0 0 0 0 4zm.8 2h3a15 15 0 0 0 1.3 3.9A8 8 0 0 1 5.1 16zm3-8h-3a8 8 0 0 1 4.3-3.9C8.8 5.3 8.4 6.6 8.1 8zM12 20c-.8-1.2-1.5-2.5-1.9-4h3.8c-.4 1.5-1.1 2.8-1.9 4zm2.3-6H9.7a14 14 0 0 1 0-4h4.6a14 14 0 0 1 0 4zm.3 5.9c.6-1.2 1-2.5 1.3-3.9h3a8 8 0 0 1-4.3 3.9zm1.7-5.9a16 16 0 0 0 0-4h3.4a8 8 0 0 1 0 4z"/></svg>
          www.novaradev.com
        </li>
      </ul>
    </div>
  </section>

  <section class="card card--back" aria-label="Business card back">
    <div class="wordmark"><span class="wordmark__dot"></span>Novara</div>
    <p class="site-address">www.novaradev.com</p>
  </section>

</main>
</body>
</html>
```